Harrowgate Estates Business Card for Apartment Buildings

Create business cards for resident managers who run apartment buildings. The audience is the public who are searching for apartment rentals, and current residents who live at the apartment building. Key design element will be incorporating the company logo, however, the logo cannot dominate. The building name and manager name are more important than the logo. Current business card design leaves little room for copy, so we may need to reduce the size on the current card to allow for more space for copy.

Target Market(s)

Adults 18-65 years of age, who are looking for an apartment rental, plus current residents who live at our apartment buildings.

Industry/Entity Type

Property Management

Contact Information for Business Card

A major design element will be use of the company logo. Important property and manager contact information must be part of the design. The size of the logo will need to be reduced to make room for building and manager contact copy.

Font styles to use
Sans Serif

Colors
3176b5
000000
959595
ffffff

Requirements
Must have
• 1) Incorporate the company logo.
• 2) Use the company colors (dark blue, black/grey, over white).
• 3) FEATURE THE BUILDING NAME
• 4) FEATURE THE MANAGER NAME
• 5) The company name is less important than BUILDING and MANAGER
• 6) Manager contact information
• **SEE ATTACHED CREATIVE BRIEF**
Nice to have
• 1) Back of card logo watermark
• 2) Ability to write notes on back of carfd
Should not have
• Avoid letting the company logo dominate the card, the building name and manager are more important than the company logo.

```html
<!DOCTYPE html>
<html lang="en">
<head>
<meta charset="utf-8">
<title>Harrowgate Estates Business Card</title>
<link href="https://fonts.googleapis.com/css2?family=Poppins:wght@400;500;600&family=Open+Sans:wght@400&display=swap" rel="stylesheet">
<style>
  :root {
    --brand-blue: #3176b5;
    --band-blue: #1f6fb0;
    --ink: #3a3a3a;
    --grey: #959595;
    --paper: #ffffff;
    --backdrop: #e7e8ea;
    --watermark: #eef0f3;
  }
  * { margin: 0; padding: 0; box-sizing: border-box; }
  html, body { width: 1200px; height: 1029px; overflow: hidden; background: var(--backdrop); }
  .card {
    position: absolute;
    top: 333px;
    width: 497px;
    height: 282px;
    background: var(--paper);
    border: 1px solid #9a9a9a;
    overflow: hidden;
  }
  .card-front { left: 80px; }
  .card-back { left: 612px; }

  .company-name {
    position: absolute;
    left: 33px; top: 36px;
    display: flex; align-items: center; gap: 8px;
    font-family: "Poppins", sans-serif;
    font-weight: 600;
    font-size: 19px;
    color: var(--brand-blue);
    letter-spacing: 0.3px;
  }
  .company-name .dot {
    width: 24px; height: 24px; border-radius: 50%;
    background: var(--brand-blue);
  }

  .manager {
    position: absolute;
    right: 50px; top: 92px;
    text-align: right;
    font-family: "Poppins", sans-serif;
  }
  .manager-name { font-size: 21px; font-weight: 400; color: var(--band-blue); line-height: 1.2; }
  .manager-title { font-family: "Open Sans", sans-serif; font-size: 12.5px; color: var(--ink); margin-top: 4px; letter-spacing: 0.3px; }

  .contact-list {
    position: absolute;
    right: 50px; top: 180px;
    list-style: none;
    text-align: right;
    font-family: "Open Sans", sans-serif;
    font-size: 13.5px;
    line-height: 18px;
    color: var(--ink);
  }
  .address {
    position: absolute;
    left: 18px; top: 217px;
    font-family: "Open Sans", sans-serif;
    font-size: 13.5px;
    line-height: 18px;
    color: var(--ink);
  }
  .side-band { position: absolute; right: 0; top: 0; width: 39px; height: 100%; }
  .bottom-band { position: absolute; left: 0; bottom: 0; }

  .back-mark {
    position: absolute; inset: 0;
    display: flex; align-items: center; justify-content: center;
    font-family: "Poppins", sans-serif;
    font-weight: 600;
    font-size: 34px;
    color: var(--watermark);
    letter-spacing: 1px;
  }
</style>
</head>
<body>

<section class="card card-front" aria-label="Business card front">
  <div class="company-name"><span class="dot"></span>HARROWGATE ESTATES</div>

  <div class="manager">
    <p class="manager-name">DANIEL WHITFIELD</p>
    <p class="manager-title">Property Manager</p>
  </div>

  <ul class="contact-list">
    <li>555 014 2287</li>
    <li>555 017 6043</li>
    <li>daniel@harrowgateestates.us</li>
    <li>www.harrowgateestates.us</li>
  </ul>

  <p class="address">2871 Larkspur Valley Road B210<br>Fairhaven, CA 90412</p>

  <svg class="side-band" viewBox="0 0 39 282" width="39" height="282" aria-hidden="true">
    <rect x="0" y="0" width="39" height="282" fill="var(--band-blue)"/>
    <polygon points="0,91 13,102.5 0,114" fill="#ffffff"/>
    <!-- phone -->
    <path d="M10 182 q0 -3 3 -3 h8 q3 0 3 3 v2 h-3 v-1.5 h-8 v1.5 h-3 z" fill="#ffffff"/>
    <rect x="12" y="185" width="10" height="4" rx="1" fill="#ffffff"/>
    <!-- printer -->
    <rect x="13" y="198" width="8" height="4" fill="#ffffff"/>
    <rect x="10" y="202" width="14" height="6" rx="1" fill="#ffffff"/>
    <!-- envelope -->
    <rect x="10" y="218" width="14" height="9" rx="1" fill="#ffffff"/>
    <polyline points="10.5,218.5 17,223.5 23.5,218.5" fill="none" stroke="var(--band-blue)" stroke-width="1"/>
    <!-- globe -->
    <circle cx="17" cy="240" r="5.5" fill="none" stroke="#ffffff" stroke-width="1.3"/>
    <ellipse cx="17" cy="240" rx="2.3" ry="5.5" fill="none" stroke="#ffffff" stroke-width="1"/>
    <line x1="11.5" y1="240" x2="22.5" y2="240" stroke="#ffffff" stroke-width="1"/>
  </svg>

  <svg class="bottom-band" viewBox="0 0 300 17" width="300" height="17" aria-hidden="true">
    <polygon points="0,0 275,0 295,17 0,17" fill="var(--band-blue)"/>
  </svg>
</section>

<section class="card card-back" aria-label="Business card back">
  <div class="back-mark">HARROWGATE ESTATES</div>
</section>

</body>
</html>
```